Brightfern World Learning is to provide global summer programs in the United States through which students from the US and China share experiences, intensive learning, and each other’s cultures. The program seeks to more fully prepare both the US and Chinese students for their college education and future careers in this interdependent world. Chinese students are individually paired with US Students where they will reside US students' home for the period of the program.

Current website: Brightfern World Learning

Need to support both English and Chinese with different font.

Project Deadline Extended
Reason: Because of Thanksgiving Holidays.

Dear Designers,

In order to generate the best design, I uploaded some photos from our global summer program. Please check:

http://brightfernworldlearning.org/photos/

Colette

My company Logo just added to the project.

Sorry for the late update.

Project Deadline Extended
Reason: Due to Thanksgiving holiday, I don't have enough time to provide feedback to all the designers. Colette

Project Deadline Extended
Reason: Holiday season. Need more time for designer and myself.

Target Market(s)

Grade K to 12 students and their parents to sign up the global summer program. Majority audience are from China.

Industry/Entity Type

College

Font styles to use
Sans Serif

Colors
3277b5

Requirements
Must have
• You may check my current website for the summer program content
www.brightfernworldlearning.org
Check these two clips to see what service we provided.
http://www.vidhaven.example/watch?v=7kR3nq41xTm&feature=vh.be
https://www.vidhaven.example/watch?v=W8d2JP6h4oZ

Company Logo are included in the attachment.

Some photos from summer program: http://brightfernworldlearning.org/photos/
The website should show the students one to one relationship.
The website should show homestay part.

I want Photo Slider on each page to share the fun activities.

Each program will be provide a video clip as a summery.

The website should support font of both English and Chinese. I like to see both Chinese and English on the same page instead of switch back and forth. I can add Chinese part later if you leave the room.

Nice to have
• I have a lot of paired pictures. I am wondering if I can use collage of photos as the background.

The design should be playful and fun!

```html
<!DOCTYPE html>
<html lang="en">
<head>
<meta charset="utf-8">
<title>Brightfern World Learning</title>
<link rel="stylesheet" href="https://fonts.googleapis.com/css2?family=Open+Sans:ital,wght@0,400;0,600;0,700;1,400&display=swap">
<style>
:root{
  --brand:#3277b5;
  --brand-dark:#25598a;
  --navy:#1b2533;
  --ink:#333b44;
  --muted:#7b8590;
  --sky:#e8f2fa;
  --night:#1c1f24;
  --white:#ffffff;
  --rule:#d9dee3;
}
*{box-sizing:border-box;margin:0;padding:0}
html,body{width:1200px;height:3556px;overflow:hidden}
body{font-family:"Open Sans",Arial,sans-serif;color:var(--ink);background:var(--white);position:relative}
.abs{position:absolute}
.fill{position:absolute;border-radius:2px}

/* header */
.topbar{left:0;top:0;width:1200px;height:88px;background:var(--brand)}
.brand{left:60px;top:18px;display:flex;align-items:center;gap:14px}
.brand-dot{width:50px;height:50px;border-radius:50%;background:var(--white)}
.brand-name{font-size:22px;font-weight:700;color:var(--white)}
.brand-tag{left:250px;top:31px;color:var(--white);font-size:15px;opacity:.9}
.langs{right:110px;top:22px;display:flex;gap:8px}
.flag{width:26px;height:18px}
.search{right:50px;top:16px;width:44px;height:34px;background:var(--white);display:flex;align-items:center;justify-content:center}
.nav{left:0;top:88px;width:1200px;height:60px;background:var(--navy);display:flex;padding-left:60px}
.nav a{color:var(--white);font-size:13px;font-weight:700;text-decoration:none;padding:0 17px;line-height:60px;letter-spacing:.2px;white-space:nowrap}
.nav a.active{background:var(--brand)}
.dropdown{left:410px;top:148px;width:570px;height:128px;background:var(--navy);z-index:5;display:flex;padding:10px 16px;gap:16px}
.dropdown ul{list-style:none;width:240px;border-right:1px solid #3a4656}
.dropdown li{color:#cfd8e2;font-size:12px;line-height:21px;border-bottom:1px solid #2c3746}
.dropdown p{color:#cfd8e2;font-size:12px;line-height:17px;width:150px}
.drop-photo{width:110px;height:100px;background:linear-gradient(135deg,#8cb070,#d9c7a2)}

/* slider */
.hero{left:0;top:148px;width:1200px;height:412px;background:var(--sky)}
.hero-media{left:120px;top:160px;width:420px;height:380px;background:linear-gradient(160deg,#b8c9d8,#7d6a58 60%,#c14b3f)}
.hero-text{left:600px;top:360px;width:500px;font-size:15px;line-height:22px;color:var(--ink)}
.btn{display:inline-block;background:var(--brand);color:var(--white);font-weight:700;font-size:14px;padding:10px 20px}
.hero-btn{left:600px;top:450px}
.arrow{width:34px;height:42px;background:var(--brand);display:flex;align-items:center;justify-content:center}

/* section titles */
.band{left:0;width:1200px;background:var(--brand)}
.band-title{color:var(--white);font-size:30px;font-weight:600;left:60px}
.plain-title{color:var(--brand);font-size:30px;font-weight:600;left:60px}

/* gallery */
.gallery{left:0;top:712px;width:1200px;height:628px;background:#0b0c0e}
.tile-icons{display:flex;gap:8px;position:absolute;left:150px;top:805px}
.tile-icons span{width:34px;height:34px;background:var(--brand);display:flex;align-items:center;justify-content:center}

/* projects */
.proj-square{width:148px;height:118px}
.proj-circle{width:48px;height:48px;border-radius:50%;background:var(--white);border:3px solid var(--brand)}
.proj h3{font-size:20px;font-weight:600;color:var(--ink);margin-bottom:8px}
.proj p{font-size:13px;line-height:19px;color:var(--muted)}
.proj .more{color:var(--brand);font-weight:700;font-size:13px}

/* about */
.about-bg{left:0;top:1780px;width:1200px;height:440px;background:linear-gradient(180deg,#3c5a7a,#23384f)}
.about-headline{left:100px;width:1000px;top:1880px;text-align:center;color:var(--white);font-size:30px;font-weight:700;line-height:40px}
.about-sub{left:200px;width:800px;top:1975px;text-align:center;color:#d8e4ef;font-size:14px}
.about-btn{left:543px;top:2040px}

/* testimonials */
.avatar{width:84px;height:84px;background:linear-gradient(135deg,#a9c0d4,#6d8297)}
.testi h4{color:var(--brand);font-size:17px;font-weight:600;margin-bottom:6px}
.testi p{font-size:13px;line-height:19px;color:var(--muted)}

/* social feed */
.feed{left:0;top:2760px;width:1200px;height:112px;background:var(--brand)}
.feed-icon{left:60px;top:2760px;width:240px;height:112px;background:var(--brand-dark);display:flex;align-items:center;gap:14px;padding-left:40px;color:var(--white);font-size:14px}
.feed-text{left:340px;width:800px;text-align:center;top:2804px;color:var(--white);font-style:italic;font-size:15px}

/* dark */
.dark{left:0;top:2872px;width:1200px;height:568px;background:var(--night)}
.dark-title{color:var(--white);font-size:26px;font-weight:700}
.thumb{width:170px}
.thumb .img{height:112px}
.thumb .meta{background:var(--white);height:24px;font-size:11px;color:var(--ink);display:flex;align-items:center;gap:6px;padding-left:8px}
.thumb .go{background:var(--brand);height:26px;color:var(--white);font-size:12px;text-align:center;line-height:26px}
.news p{color:#b9c0c8;font-size:12px;line-height:18px}
.field{background:var(--white);height:36px;width:330px;color:var(--muted);font-size:12px;line-height:36px;padding-left:10px}
.contact{color:#c9d0d8;font-size:13px;line-height:22px}

/* footer */
.footer{left:0;top:3440px;width:1200px;height:116px;background:var(--brand)}
.foot-copy{left:0;width:1200px;text-align:center;top:3490px;color:var(--white);font-size:12px}
.soc{width:32px;height:32px;background:var(--navy)}
</style>
</head>
<body>

<header>
  <div class="abs topbar"></div>
  <div class="abs brand"><span class="brand-dot"></span><span class="brand-name">Brightfern</span></div>
  <div class="abs brand-tag">Nurture Global Citizens and Global Leaders</div>
  <div class="abs langs">
    <svg class="flag" viewBox="0 0 26 18"><rect width="26" height="18" fill="#d7262b"/></svg>
    <svg class="flag" viewBox="0 0 26 18"><rect width="26" height="18" fill="#f2f2f2"/><rect width="26" height="3" y="3" fill="#c8333a"/><rect width="26" height="3" y="9" fill="#c8333a"/><rect width="26" height="3" y="15" fill="#c8333a"/><rect width="11" height="9" fill="#2f4a8a"/></svg>
  </div>
  <div class="abs search"><svg width="18" height="18" viewBox="0 0 18 18"><circle cx="7.5" cy="7.5" r="5.5" fill="none" stroke="#1b2533" stroke-width="2"/><line x1="11.5" y1="11.5" x2="16.5" y2="16.5" stroke="#1b2533" stroke-width="2.4"/></svg></div>
  <nav class="abs nav">
    <a>HOME</a><a>HALDEN SUMMER PROGRAM ▾</a><a class="active">OAKWAY YOUTH CAMP ▾</a><a>WHOLE YEAR PROGRAM ▾</a><a>MARLOWE UNIVERSITY ▾</a><a>CONTACT</a>
  </nav>
  <div class="abs dropdown">
    <ul><li>Cheerleading Camp</li><li>Gymnastics Camp</li><li>Sports Camp</li><li>Kids in the Kitchen Camp</li><li>Community Time Camp</li></ul>
    <p>Cheerleading camp for kids of all ages with coaches, games and a final show.</p>
    <div class="drop-photo" role="img" aria-label="Photo of campers smiling together outdoors"></div>
  </div>
</header>

<section>
  <div class="abs hero"></div>
  <div class="abs hero-media" role="img" aria-label="Video still of students holding flags at a summer program event"></div>
  <p class="abs hero-text">Our summer programs let students from the US and China live, learn and have fun together under teachers' guidance.</p>
  <span class="abs btn hero-btn">READ MORE</span>
  <div class="abs arrow" style="left:30px;top:370px"><svg width="12" height="16" viewBox="0 0 12 16"><path d="M10 1 3 8l7 7" fill="none" stroke="#fff" stroke-width="3"/></svg></div>
  <div class="abs arrow" style="left:1136px;top:370px"><svg width="12" height="16" viewBox="0 0 12 16"><path d="M2 1l7 7-7 7" fill="none" stroke="#fff" stroke-width="3"/></svg></div>
</section>

<section>
  <div class="abs band" style="top:572px;height:140px"></div>
  <h2 class="abs band-title" style="top:600px">Picture Gallery</h2>
  <div class="abs gallery"></div>
  <div class="fill" style="left:100px;top:745px;width:240px;height:180px;background:linear-gradient(135deg,#3a79b9,#8fb4d6)" role="img" aria-label="Students posing in matching shirts"></div>
  <div class="fill" style="left:352px;top:745px;width:240px;height:180px;background:linear-gradient(135deg,#b2c1cc,#6f7c86)" role="img" aria-label="Group photo at a city landmark"></div>
  <div class="fill" style="left:604px;top:745px;width:240px;height:180px;background:linear-gradient(135deg,#c4d3c0,#7f9a6c)" role="img" aria-label="Students outdoors in a park"></div>
  <div class="fill" style="left:856px;top:745px;width:240px;height:180px;background:linear-gradient(135deg,#cdb8a3,#8a6e5b)" role="img" aria-label="Host family and student together"></div>
  <div class="fill" style="left:100px;top:937px;width:240px;height:180px;background:linear-gradient(135deg,#d9a68a,#9c5f4a)" role="img" aria-label="Students at a campus event"></div>
  <div class="fill" style="left:352px;top:937px;width:240px;height:180px;background:linear-gradient(135deg,#a8c4d9,#5a6f83)" role="img" aria-label="Group by a city skyline"></div>
  <div class="fill" style="left:604px;top:937px;width:240px;height:180px;background:linear-gradient(135deg,#9ab6cf,#486683)" role="img" aria-label="Students on a lakefront walk"></div>
  <div class="fill" style="left:856px;top:937px;width:240px;height:180px;background:linear-gradient(135deg,#c9b39a,#6d5a48)" role="img" aria-label="Paired students in a classroom"></div>
  <div class="fill" style="left:100px;top:1129px;width:240px;height:180px;background:linear-gradient(135deg,#e0c089,#a4734f)" role="img" aria-label="Students on a field trip"></div>
  <div class="fill" style="left:352px;top:1129px;width:240px;height:180px;background:linear-gradient(135deg,#d4a46b,#a35d3b)" role="img" aria-label="Students smiling at an activity"></div>
  <div class="fill" style="left:604px;top:1129px;width:240px;height:180px;background:linear-gradient(135deg,#a9c3df,#5c84ad)" role="img" aria-label="Group at a waterfront"></div>
  <div class="fill" style="left:856px;top:1129px;width:240px;height:180px;background:linear-gradient(135deg,#9dc2dc,#4e7ea6)" role="img" aria-label="City harbor view on a group outing"></div>
  <div class="tile-icons">
    <span><svg width="16" height="16" viewBox="0 0 16 16"><path d="M3 13 13 3M8 3h5v5" fill="none" stroke="#fff" stroke-width="2"/></svg></span>
    <span><svg width="16" height="16" viewBox="0 0 16 16"><circle cx="7" cy="7" r="4.5" fill="none" stroke="#fff" stroke-width="2"/><line x1="10" y1="10" x2="14" y2="14" stroke="#fff" stroke-width="2"/></svg></span>
  </div>
</section>

<section>
  <h2 class="abs plain-title" style="top:1348px">Projects</h2>
  <div class="abs" style="left:60px;top:1400px;width:1080px;height:1px;background:var(--rule)"></div>
  <div class="abs proj-square" style="left:452px;top:1420px;background:#eef3f7"></div>
  <div class="abs proj-square" style="left:600px;top:1420px;background:var(--brand)"></div>
  <div class="abs proj-square" style="left:452px;top:1538px;background:var(--brand)"></div>
  <div class="abs proj-square" style="left:600px;top:1538px;background:#eef3f7"></div>
  <div class="abs proj-circle" style="left:476px;top:1455px"></div>
  <div class="abs proj-circle" style="left:676px;top:1455px"></div>
  <div class="abs proj-circle" style="left:476px;top:1573px"></div>
  <div class="abs proj-circle" style="left:676px;top:1573px"></div>
  <div class="abs proj" style="left:100px;top:1424px;width:330px;text-align:right"><h3>Halden Summer Program</h3><p>Halden School pairs each visiting student with a local partner and host family.</p><span class="more">More...</span></div>
  <div class="abs proj" style="left:770px;top:1424px;width:330px"><h3>Oakway Youth Summer Camp</h3><p>A camp full of sports, kitchen fun and teamwork alongside local kids.</p><span class="more">More...</span></div>
  <div class="abs proj" style="left:100px;top:1542px;width:330px;text-align:right"><h3>Whole Year Program</h3><p>Students live with a host family for a full school year with their partners.</p><span class="more">More...</span></div>
  <div class="abs proj" style="left:770px;top:1542px;width:330px"><h3>Marlowe University</h3><p>Our partner university offers campus stays, classes and future planning.</p><span class="more">More...</span></div>
</section>

<section>
  <div class="abs band" style="top:1700px;height:80px"></div>
  <h2 class="abs band-title" style="top:1718px">About Brightfern World Learning</h2>
  <div class="abs about-bg" role="img" aria-label="Collage of paired student photos behind a blue tint"></div>
  <h2 class="abs about-headline">We Focus on one to one Paired homestay Program with Intensive<br>Academic Learning and Culture Exchange</h2>
  <p class="abs about-sub">Brightfern World Learning brings US and Chinese students together to share study, homes and cultures.</p>
  <span class="abs btn about-btn">READ MORE</span>
</section>

<section>
  <h2 class="abs plain-title" style="top:2262px">Testimonials</h2>
  <div class="abs" style="left:60px;top:2316px;width:1080px;height:1px;background:var(--rule)"></div>
  <div class="abs avatar" style="left:100px;top:2400px" role="img" aria-label="Portrait of a parent"></div>
  <div class="abs testi" style="left:200px;top:2400px;width:330px"><h4>Jonah Abbott</h4><p>My son made a true friend and learned so much. The host family was warm and kind. <span style="color:var(--brand)">Read More</span></p></div>
  <div class="abs avatar" style="left:620px;top:2400px" role="img" aria-label="Portrait of a parent"></div>
  <div class="abs testi" style="left:720px;top:2400px;width:330px"><h4>Zhou Lan</h4><p>Our daughter came home confident and excited about college. A great summer for her. <span style="color:var(--brand)">Read More</span></p></div>
  <div class="abs" style="left:100px;top:2540px;width:440px;height:1px;background:var(--rule)"></div>
  <div class="abs" style="left:620px;top:2540px;width:440px;height:1px;background:var(--rule)"></div>
  <div class="abs avatar" style="left:100px;top:2580px" role="img" aria-label="Portrait of a student"></div>
  <div class="abs testi" style="left:200px;top:2580px;width:330px"><h4>Xia Lin</h4><p>I lived with my partner's family and joined every camp day. I miss them already. <span style="color:var(--brand)">Read More</span></p></div>
  <div class="abs avatar" style="left:620px;top:2580px" role="img" aria-label="Portrait of a host parent"></div>
  <div class="abs testi" style="left:720px;top:2580px;width:330px"><h4>Sabrina Tolle</h4><p>Hosting a student opened our home to a new culture. We plan to host again next year. <span style="color:var(--brand)">Read More</span></p></div>
</section>

<section>
  <div class="abs feed"></div>
  <div class="abs feed-icon"><svg width="26" height="26" viewBox="0 0 26 26"><circle cx="13" cy="13" r="12" fill="#fff"/></svg>Social feed</div>
  <p class="abs feed-text">Great news from our summer students — new photos from camp week are now online!</p>
</section>

<section>
  <div class="abs dark"></div>
  <h3 class="abs dark-title" style="left:60px;top:2900px">Recent Posts</h3>
  <h3 class="abs dark-title" style="left:640px;top:2900px">Recent Projects</h3>
  <div class="abs thumb" style="left:60px;top:2950px"><div class="img" style="background:linear-gradient(135deg,#c98b63,#7b5a49)" role="img" aria-label="Post photo of students"></div><div class="meta">▣ 22/12/2015</div><div class="go">Read more</div></div>
  <div class="abs thumb" style="left:240px;top:2950px"><div class="img" style="background:linear-gradient(135deg,#8fb0cd,#53708e)" role="img" aria-label="Post photo of a group outing"></div><div class="meta">▣ 22/12/2015</div><div class="go">Read more</div></div>
  <div class="abs thumb" style="left:420px;top:2950px"><div class="img" style="background:linear-gradient(135deg,#d2b08b,#8d6b52)" role="img" aria-label="Post photo of host families"></div><div class="meta">▣ 22/12/2015</div><div class="go">Read more</div></div>
  <div class="abs thumb" style="left:640px;top:2950px"><div class="img" style="background:linear-gradient(135deg,#b7c6d3,#5f7488)" role="img" aria-label="Project photo of a campus"></div><div class="meta">▣ 22/12/2015</div><div class="go">Read more</div></div>
  <div class="abs thumb" style="left:820px;top:2950px"><div class="img" style="background:linear-gradient(135deg,#a7bf9a,#5f7a55)" role="img" aria-label="Project photo of a camp"></div><div class="meta">▣ 22/12/2015</div><div class="go">Read more</div></div>
  <div class="abs thumb" style="left:1000px;top:2950px;width:140px"><div class="img" style="background:linear-gradient(135deg,#cfa17e,#83604a)" role="img" aria-label="Project photo of a class"></div><div class="meta">▣ 22/12/2015</div><div class="go">Read more</div></div>
  <h3 class="abs dark-title" style="left:60px;top:3150px">Newsletter Sign Up</h3>
  <div class="abs news" style="left:60px;top:3196px;width:480px"><p>By subscribing to our mailing list you will always get latest news and updates from us.</p></div>
  <div class="abs field" style="left:60px;top:3250px">Email...</div>
  <span class="abs btn" style="left:400px;top:3250px;height:36px;padding:0 40px;line-height:36px;font-size:12px">SIGN UP</span>
  <h3 class="abs dark-title" style="left:640px;top:3150px">Contact Us</h3>
  <div class="abs contact" style="left:640px;top:3196px;width:500px">
    <p>☎ Tel: 555-0142-7788 &nbsp;&nbsp; ☎ Fax: 555-0142-7790</p>
    <p>✉ info@brightfernworldlearning.org</p>
    <p>⌂ Address:</p>
    <p>Kestrel College of Commerce, Marlowe University<br>410 Linden Park Way<br>Fairhollow, IL 60999</p>
  </div>
</section>

<footer>
  <div class="abs footer"></div>
  <div class="abs brand" style="top:3473px"><span class="brand-dot"></span><span class="brand-name">Brightfern</span></div>
  <p class="abs foot-copy">2015 Copyright Brightfern World Learning. All Rights Reserved</p>
  <div class="abs" style="left:1040px;top:3460px;display:grid;grid-template-columns:repeat(3,32px);gap:6px">
    <span class="soc"></span><span class="soc"></span><span class="soc"></span>
    <span class="soc"></span><span class="soc" style="background:#d7262b"></span><span class="soc"></span>
  </div>
</footer>

</body>
</html>
```